Startup online payment business - Sporting / Golf, Swift Tee payment

Background:
Our business name is "Swift Tee" we provide online payments for golfing services via our website. We currently have a logo used on our website. No other design style has been developed. Our aim is to remove cash payments for service at golf clubs.

Our Key Values:
Quick and easy
Formal and polite
Fun with professional boundary
Mate-ship relationships
100% online digital

What we want from you:
Marketing design to be used on posters and stickers in a retail setting to direct customers to our online payment Chanel.
Design must incorporate attached logo, URL swifttee.com.au and our key values can act as a guide the type of design. We have used color Hex#007672 for logo background. We are open to use other colors.

Target Market(s)

Golf clubs and golf players

Industry/Entity Type

Golf Course

Font styles to use
Sans Serif

Requirements
Must have
• Directions to online payment via URL: swifttee.com.au
Nice to have
• We like the idea of the slogan: No Cash - No worries. Have attached home screen that will be available from URL link. Consideration if using mobile phone in image. Push the online payment and steps 1. Visit swifttee.com 2. Select club 3. Confirm payment
Should not have
• Cartoons

```html
<!DOCTYPE html>
<html lang="en">
<head>
<meta charset="utf-8">
<title>Swift Tee – No Cash No Worries</title>
<link rel="stylesheet" href="https://fonts.googleapis.com/css2?family=Montserrat:wght@600&family=Source+Sans+3:wght@300;400;600;700&display=swap">
<style>
  :root {
    --teal: #0f7b76;
    --teal-text: #137c77;
    --green: #2ea843;
    --ink: #121820;
    --slate: #24394a;
    --text-dark: #14202a;
    --white: #ffffff;
    --stage: #1f1f21;
  }
  * { margin: 0; padding: 0; box-sizing: border-box; }
  html, body { width: 1200px; height: 1195px; overflow: hidden; background: var(--stage); }
  .poster {
    position: absolute; left: 178px; top: 0; width: 844px; height: 1195px;
    overflow: hidden; background: var(--white);
    font-family: "Source Sans 3", Arial, sans-serif;
  }
  .poster-shapes { position: absolute; inset: 0; }
  .txt { position: absolute; white-space: nowrap; }
  .tagline {
    right: 410px; top: 40px; text-align: right;
    font-weight: 700; font-size: 29px; line-height: 42px; color: var(--teal-text);
  }
  .brand-name {
    left: 60px; width: 400px; top: 410px; text-align: center;
    font-weight: 700; font-size: 50px; letter-spacing: 4px; color: var(--white);
  }
  .slogan {
    right: 58px; top: 496px; text-align: right;
    font-family: "Montserrat", Arial, sans-serif; font-weight: 600;
    font-size: 58px; line-height: 67px; color: var(--white);
  }
  .directions {
    right: 58px; top: 646px; text-align: right;
    font-weight: 700; font-size: 21px; line-height: 34px; color: var(--green);
  }
  .directions .url { font-size: 26px; }
  .about-title {
    left: 274px; top: 746px; font-weight: 300; font-size: 31px; color: var(--text-dark);
  }
  .about-copy {
    left: 274px; top: 800px; width: 530px; white-space: normal;
    font-weight: 700; font-size: 15.6px; line-height: 21.5px; color: var(--text-dark);
  }
  .about-copy p + p { margin-top: 9px; }
  .values-label {
    left: 274px; top: 955px; font-weight: 700; font-size: 19px; color: var(--white);
  }
  .values-list {
    position: absolute; left: 270px; top: 1000px; list-style: none;
    font-weight: 600; font-size: 20px; line-height: 28px; color: var(--text-dark);
  }
  .values-list li { position: relative; padding-left: 27px; }
  .values-list li::before {
    content: ""; position: absolute; left: 0; top: 9px;
    width: 14px; height: 14px; border-radius: 50%; background: #243845;
  }
  .contact-label {
    left: 312px; top: 1162px; transform: translateX(-50%);
    font-weight: 700; font-size: 19px; letter-spacing: 1.5px; color: var(--white);
  }
  .contact-details {
    left: 460px; top: 1161px; font-weight: 400; font-size: 18px; color: var(--white);
  }
  .contact-details .sep { opacity: .8; margin: 0 8px 0 0; }
  .contact-details .sep + .sep, .contact-details .gap { margin-left: 8px; }
</style>
</head>
<body>
<main class="poster">
  <svg class="poster-shapes" viewBox="0 0 844 1195" width="844" height="1195" aria-hidden="false">
    <defs>
      <linearGradient id="sunset" x1="0" y1="0" x2="0" y2="1">
        <stop offset="0" stop-color="#1fb5cf"/>
        <stop offset="0.45" stop-color="#8fb9b0"/>
        <stop offset="0.75" stop-color="#f39a45"/>
        <stop offset="1" stop-color="#e5701f"/>
      </linearGradient>
      <linearGradient id="putting" x1="0" y1="0" x2="0" y2="1">
        <stop offset="0" stop-color="#d9eef8"/>
        <stop offset="0.3" stop-color="#8fb9cf"/>
        <stop offset="0.4" stop-color="#6f9a4d"/>
        <stop offset="1" stop-color="#4f8a33"/>
      </linearGradient>
      <linearGradient id="card" x1="0" y1="0" x2="1" y2="1">
        <stop offset="0" stop-color="#e7e4e0"/>
        <stop offset="0.5" stop-color="#e0753a"/>
        <stop offset="1" stop-color="#5b4a40"/>
      </linearGradient>
      <linearGradient id="laptop" x1="0" y1="0" x2="1" y2="1">
        <stop offset="0" stop-color="#f2f2f0"/>
        <stop offset="0.5" stop-color="#dfe0de"/>
        <stop offset="1" stop-color="#c9c6c1"/>
      </linearGradient>
      <linearGradient id="green-blur" x1="0" y1="0" x2="0" y2="1">
        <stop offset="0" stop-color="#e3ebe0"/>
        <stop offset="0.5" stop-color="#c9d9c0"/>
        <stop offset="1" stop-color="#a9bd9d"/>
      </linearGradient>
    </defs>

    <!-- dark frame and bands -->
    <polygon fill="var(--ink)" points="0,0 30,0 260,205 525,470 844,470 844,716 246,716 141,825 141,1195 0,1195"/>

    <rect role="img" aria-label="Photo: smiling woman sitting cross-legged in a chair with a laptop" fill="url(#laptop)" x="484" y="0" width="360" height="470"/>

    <polygon role="img" aria-label="Photo: silhouette of a woman golfer swinging against a sunset sky" fill="url(#sunset)" points="0,35 218,252 0,468"/>
    <polygon role="img" aria-label="Photo: golfer putting on a sunny green" fill="url(#putting)" points="0,500 212,712 0,928"/>
    <polygon role="img" aria-label="Photo: close-up of a payment card" fill="url(#card)" points="141,870 141,1120 12,992"/>

    <line x1="0" y1="485" x2="242" y2="727" stroke="var(--green)" stroke-width="15"/>
    <line x1="0" y1="940" x2="242" y2="716" stroke="var(--green)" stroke-width="13"/>
    <polygon fill="var(--green)" points="0,1003 0,1195 200,1195"/>

    <polygon role="img" aria-label="Photo: blurred golf ball on the green beside the hole" fill="url(#green-blur)" points="246,716 844,716 844,1195 141,1195 141,825"/>

    <!-- footer band -->
    <polygon fill="var(--ink)" points="150,1155 410,1155 450,1195 190,1195"/>
    <polygon fill="var(--slate)" points="410,1155 844,1155 844,1195 450,1195"/>

    <!-- brand diamond -->
    <polygon fill="var(--green)" points="260,231 491,470 260,700 27,470"/>
    <polygon fill="var(--teal)" points="260,261 469,470 260,678 53,470"/>

    <!-- key values label bar -->
    <path fill="var(--green)" d="M262,952 H766 Q776,952 772,960 L764,976 Q760,984 750,984 H258 Q248,984 252,976 L256,960 Q258,952 262,952 Z"/>

    <line x1="551" y1="1163" x2="551" y2="1187" stroke="var(--white)" stroke-width="1" opacity=".8"/>
  </svg>

  <div class="txt tagline">Online payments<br>for golfing services</div>
  <div class="txt brand-name">SWIFT TEE</div>
  <div class="txt slogan">No Cash<br>No Worries</div>
  <div class="txt directions">Directions to online payment via URL:<br><span class="url">www.swifttee.com.au</span></div>

  <h2 class="txt about-title">ABOUT US</h2>
  <div class="txt about-copy">
    <p>Swift Tee is here to support Golf Clubs embrace new strategies for success in a rapidly changing world.</p>
    <p>Moving toward a future cashless society, Swift Tee are developing new mobile payment methods in order for Clubs to cater for the next generation of players and community expectations.</p>
  </div>

  <div class="txt values-label">OUR KEY VALUES:</div>
  <ul class="values-list">
    <li>Quick and easy</li>
    <li>Formal and polite</li>
    <li>Fun with professional boundary</li>
    <li>Mate-ship relationships</li>
    <li>100% online digital</li>
  </ul>

  <div class="txt contact-label">CONTACT US</div>
  <div class="txt contact-details"><span class="sep">|</span>012.555.0142<span class="gap"></span><span class="sep">&nbsp;</span>info@swifttee.com.au</div>
</main>
</body>
</html>
```